Corporate Business Card

Very professional, Modern, Not to busy, include phone address email, website
(253) 555-0174, 61807 19th Street N, Kent, WA 98517, marcus@kestrelbayholding.com, brelvanindustries.com

Target Market(s)

Manufacturing

Industry/Entity Type

Aero, machining, manufacturing, Off road racing

Contact Information for Business Card

Phone, address email, website

```html
<!DOCTYPE html>
<html lang="en">
<head>
<meta charset="utf-8">
<title>Brelvan Industries – Business Card</title>
<link rel="stylesheet" href="https://fonts.googleapis.com/css2?family=Source+Sans+3:wght@400;600&display=swap">
<style>
  :root {
    --navy: #16356c;
    --red: #d3232a;
    --white: #ffffff;
    --backdrop: #999a99;
  }
  * { box-sizing: border-box; margin: 0; padding: 0; }
  html, body { width: 1200px; height: 1200px; overflow: hidden; }
  body {
    background: var(--backdrop);
    font-family: "Source Sans 3", sans-serif;
    position: relative;
  }
  .card {
    position: absolute;
    left: 232px;
    width: 736px;
    height: 452px;
    border-radius: 40px;
    overflow: hidden;
  }
  .card-front { top: 116px; background: var(--white); }
  .card-back { top: 632px; background: var(--navy); }
  .front-shape { position: absolute; inset: 0; width: 100%; height: 100%; }

  .brand {
    position: absolute;
    font-weight: 600;
    white-space: nowrap;
    letter-spacing: 0.5px;
  }
  .brand-front {
    right: 46px;
    top: 70px;
    font-size: 44px;
    color: var(--navy);
  }
  .brand-back {
    left: 0; right: 0;
    top: 186px;
    text-align: center;
    font-size: 66px;
    color: var(--white);
  }

  .person { position: absolute; left: 44px; top: 212px; color: var(--white); }
  .person-name { font-size: 36px; font-weight: 400; line-height: 1.1; }
  .person-title { font-size: 23px; color: var(--red); line-height: 1.2; }

  .contacts { position: absolute; left: 44px; top: 322px; list-style: none; }
  .contacts li {
    display: flex; align-items: center;
    height: 30.5px;
    font-size: 19.5px;
    color: var(--white);
  }
  .contacts svg { width: 20px; height: 20px; margin-right: 14px; flex: none; }

  .address {
    position: absolute;
    right: 46px;
    top: 334px;
    text-align: right;
    color: var(--white);
    font-size: 19.5px;
    line-height: 26px;
  }
  .address svg { display: block; width: 14px; height: 20px; margin-left: auto; margin-right: 0; margin-bottom: 2px; }
</style>
</head>
<body>

<section class="card card-front">
  <svg class="front-shape" viewBox="0 0 920 565" preserveAspectRatio="none" aria-hidden="true">
    <path d="M0,20 L15,15 Q450,305 920,310 L920,565 L0,565 Z" fill="var(--red)"/>
    <path d="M0,40 L15,22 Q450,320 920,333 L920,565 L0,565 Z" fill="var(--white)"/>
    <path d="M0,44 L15,26 Q450,326 920,337 L920,565 L0,565 Z" fill="var(--navy)"/>
  </svg>

  <div class="brand brand-front">Brelvan Industries</div>

  <div class="person">
    <h1 class="person-name">Dorian Wells</h1>
    <p class="person-title">President</p>
  </div>

  <ul class="contacts">
    <li>
      <svg viewBox="0 0 24 24"><path fill="var(--red)" d="M6.6 2.5l3 4.2-2 2.3c1.3 2.8 3.6 5.1 6.4 6.4l2.3-2 4.2 3-1.5 3.6c-.3.6-1 1-1.7.9C9.6 20 4 14.4 3.1 6.7c-.1-.7.3-1.4.9-1.7z"/></svg>
      (253) 555-0174
    </li>
    <li>
      <svg viewBox="0 0 24 24"><rect x="2" y="5" width="17" height="12" fill="var(--red)"/><path d="M2 5l8.5 6.5L19 5" fill="none" stroke="var(--navy)" stroke-width="1.6"/><circle cx="19" cy="17" r="4.5" fill="var(--red)" stroke="var(--navy)" stroke-width="1"/><path d="M17 17l1.5 1.5 2.5-3" fill="none" stroke="var(--white)" stroke-width="1.3"/></svg>
      marcus@kestrelbayholding.com
    </li>
    <li>
      <svg viewBox="0 0 24 24" fill="none" stroke="var(--red)" stroke-width="1.5"><circle cx="12" cy="12" r="9.5"/><ellipse cx="12" cy="12" rx="4.2" ry="9.5"/><path d="M2.5 12h19M4 7h16M4 17h16"/></svg>
      brelvanindustries.com
    </li>
  </ul>

  <address class="address" style="font-style:normal">
    <svg viewBox="0 0 14 20"><path fill="var(--red)" d="M7 0C3.1 0 0 3 0 6.9 0 11.8 7 20 7 20s7-8.2 7-13.1C14 3 10.9 0 7 0zm0 9.5a2.6 2.6 0 110-5.2 2.6 2.6 0 010 5.2z"/></svg>
    61807 19th<br>
    Street N, Kent, WA 98517
  </address>
</section>

<section class="card card-back">
  <div class="brand brand-back">Brelvan Industries</div>
</section>

</body>
</html>
```